Lanternfield Billboard - Financial Services Company (Investments, Tax Planning and Insurance)

Our new office has a billboard directly above the office building. We'd like something eye-catching with a strong Call to Action, with the main part of the billboard being under 7 words if possible. We'd like you to include a way to get ahold of us (either our website lanternfieldllc.example or our phone number 302-418-2967. You may also include in small font something to indicate that we've been serving the area since 1980 (the DE area, the tri-state area, the Copperleaf Basin, etc.)

We offer financial planning, tax planning, and insurance, and we help our clients to focus on their goals and happiness by providing everything they need for lifelong wealth under one roof.

Our logos are attached, we use a triangle logo with green and gray. We use the tagline "experience lifelong wealth" but this does not need to be included.

Potential ideas we have seen from other financial companies-
- the concept that the driver spends more time looking at billboards than planning for their retirement
-something along the lines of "everything you need for your finances is in this building right here" planning, investments, taxes, insurance"
-don't spend your time worrying about retirement, let us help you plan for it
-are you working for your money, or is it working for you?
- retirement takes planning, we're here to help
- ready to retire? talk to us
- need investment advice?
- need help investing?
- crossing your fingers isn't a retirement plan. we can help.
- retiring soon? you need help.

Those are just general ideas, please feel free to be creative.

brand colors:
#00b585
#00b185
#000000
#ffffff
#6d6f75
#6d6f75
#6f7074
#021712
#052e24

```html
<!DOCTYPE html>
<html lang="en">
<head>
<meta charset="utf-8">
<title>Lanternfield Billboard</title>
<link href="https://fonts.googleapis.com/css2?family=Roboto+Condensed:wght@400;700&display=swap" rel="stylesheet">
<style>
  :root {
    --green: #0f9d66;
    --green-deep: #0a7a4f;
    --green-light: #2fb07c;
    --gray: #6d6f75;
    --gray-dark: #4d4f54;
    --white: #ffffff;
    --page: #d9d9d9;
    --photo-warm: #e9e3da;
    --photo-sea: #d5dde0;
  }
  * { margin: 0; padding: 0; box-sizing: border-box; }
  html, body {
    width: 1200px; height: 1200px; overflow: hidden;
    background: var(--page);
    font-family: "Roboto Condensed", "Arial Narrow", sans-serif;
  }
  .billboard {
    position: absolute; left: 50px; top: 324px;
    width: 1100px; height: 552px;
    background: var(--white); overflow: hidden;
    box-shadow: 0 2px 6px rgba(0,0,0,0.18);
  }
  .hero-photo {
    position: absolute; left: 592px; top: 200px; width: 446px; height: 352px;
    background: radial-gradient(ellipse 60% 65% at 50% 55%, var(--photo-warm) 0%, var(--photo-sea) 45%, rgba(255,255,255,0) 100%);
  }
  .billboard__shapes { position: absolute; inset: 0; }
  .headline {
    position: absolute; left: 56px; top: 78px;
    color: var(--white); font-weight: 700; font-size: 51px; line-height: 60px;
    text-transform: uppercase; letter-spacing: 0.3px;
  }
  .promise {
    position: absolute; left: 56px; top: 396px; width: 400px;
    color: var(--white); font-size: 18px; line-height: 26px;
  }
  .brand {
    position: absolute; left: 700px; top: 66px;
    display: flex; align-items: center; gap: 16px;
  }
  .brand__mark { width: 52px; height: 52px; background: var(--green); }
  .brand__name {
    color: var(--green); font-weight: 700; font-size: 62px; line-height: 1;
  }
  .contact-band {
    position: absolute; left: 614px; top: 154px; width: 450px; height: 43px;
    background: var(--green); color: var(--white);
    font-size: 24px; line-height: 43px; padding-left: 70px; white-space: nowrap;
  }
</style>
</head>
<body>
  <div class="billboard">
    <div class="hero-photo" role="img" aria-label="Photo of four friends taking a selfie together on a beach"></div>

    <svg class="billboard__shapes" width="1100" height="552" viewBox="0 0 1100 552">
      <defs>
        <linearGradient id="green-field" x1="0" y1="0" x2="1" y2="1">
          <stop offset="0" stop-color="var(--green-light)"/>
          <stop offset="0.5" stop-color="var(--green)"/>
          <stop offset="1" stop-color="var(--green-deep)"/>
        </linearGradient>
      </defs>
      <polygon points="0,0 717,0 402,552 0,552" fill="url(#green-field)" role="img" aria-label="Green-tinted photo of a smiling couple relaxing together"/>
      <rect x="0" y="374" width="545" height="106" fill="var(--gray)"/>
      <polygon points="503,374 545,355 545,374" fill="var(--gray-dark)"/>
      <polygon points="887,552 1073,229 1100,276 1100,552" fill="var(--green)"/>
      <path d="M1022,552 Q1036,458 1100,404 L1100,552 Z" fill="var(--white)"/>
      <path d="M1032,552 Q1046,466 1100,418 L1100,552 Z" fill="var(--gray)"/>
    </svg>

    <h1 class="headline">We offer<br>financial planning<br>tax planning, and<br>insurance</h1>

    <p class="promise">We help our clients to focus on their goals and happiness by providing everything they need for lifelong wealth under one roof.</p>

    <div class="brand">
      <span class="brand__mark"></span>
      <span class="brand__name">Lanternfield</span>
    </div>

    <div class="contact-band">302-418-2967 | lanternfieldllc.example</div>
  </div>
</body>
</html>
```